LumaWireHub full website re-design

I'm looking for a current, cool new design of my website, lumawirehub.com. We sell fiber optic cables and accessories. It hasn't been changed for over 10 years. I would like fresh ideas, not excessive pictures of cables. It has to be easy to navigate because we have over 5k products that we sell. The platform that our site is built on is Prestashop. I've attached many of our popular brands as well as some of our products so you can get an idea of what we sell. I also encourage you to go to our current website to see everything we offer. We are a high end brand and I want to give that impression. The winning designer will likely have ongoing work in the future because we will be making changes and additions to our site. Prestashop experience preferred! Be creative as you want. I would like banner images across the top as well.

Target Market(s)

Men 20-50

Industry/Entity Type

Technology

Coding

Coded - Design and coding required

Number of Pages Required

5+ page

Requirements
Must have
• https://www.vidstreamo.com/watch?v=Q4-RtPw7z2M
Should not have
• cartoons

```html
<!DOCTYPE html>
<html lang="en">
<head>
<meta charset="utf-8">
<title>LumaWireHub — Fiber Optic Cables</title>
<link href="https://fonts.googleapis.com/css2?family=Audiowide&family=Poppins:wght@400;500;600;700&family=Roboto:wght@400;500&family=Tinos&display=swap" rel="stylesheet">
<style>
:root{
  --maroon:#851639;
  --maroon-dark:#6d0f2d;
  --grey:#6f7074;
  --ink:#222;
  --muted:#666;
  --light:#f2f2f2;
  --white:#fff;
}
*{box-sizing:border-box;margin:0;padding:0}
html,body{width:1200px;height:3586px;overflow:hidden}
body{font-family:"Poppins",sans-serif;color:var(--ink);background:var(--white);position:relative}
.abs{position:absolute}
.display{font-family:"Audiowide",sans-serif;font-weight:400;letter-spacing:1px}
.btn{position:absolute;background:var(--maroon);color:var(--white);font:600 12px "Poppins",sans-serif;display:flex;align-items:center;justify-content:center;border-radius:4px;text-transform:uppercase}
.divider{position:absolute;height:14px;display:flex;align-items:center;gap:8px}
.divider i{display:block;height:1.5px;width:36px;background:currentColor}
.divider b{display:block;width:10px;height:10px;border:2px solid currentColor;border-radius:50%}

/* top bar */
.topbar{top:0;left:0;width:1200px;height:38px;background:var(--maroon);color:var(--white);font-size:12px}
.topbar span{position:absolute;top:11px}
.auth{position:absolute;top:5px;height:27px;background:#eee;color:var(--maroon-dark);border-radius:4px;font:600 12px "Poppins",sans-serif;display:flex;align-items:center;justify-content:center;gap:8px}
.auth i{width:18px;height:18px;border:1.5px solid var(--maroon-dark);border-radius:50%}

/* nav */
.nav{top:38px;left:0;width:1200px;height:48px;background:var(--white)}
.logo{position:absolute;left:133px;top:11px;display:flex;align-items:center;gap:6px;font:700 22px "Poppins",sans-serif;color:var(--maroon)}
.logo i{width:22px;height:22px;border-radius:50%;background:var(--maroon)}
.menu{position:absolute;left:333px;top:16px;display:flex;gap:18px;font-size:12.5px;color:#333}
.menu .active{font-weight:600}
.search{position:absolute;left:846px;top:11px;width:186px;height:27px;background:#eee;border-radius:4px;font-size:11px;color:#888;padding:6px 12px}
.search svg{position:absolute;right:10px;top:5px}

/* hero */
.hero{top:86px;left:0;width:1112px;height:500px;border-bottom-right-radius:90px;overflow:hidden;background:linear-gradient(100deg,#3d4a2a 0%,#6b7a40 30%,#8a6a4a 55%,#5a4a35 75%,#4b5a30 100%)}
.hero .shade{position:absolute;inset:0;background:rgba(0,0,0,.28)}
.hero h1{position:absolute;top:184px;left:0;width:1200px;text-align:center;color:var(--white);font-size:38px}
.hero p{position:absolute;top:243px;left:340px;width:520px;text-align:center;color:var(--white);font-size:12.5px;font-weight:600;line-height:19px}

/* about */
.about-title{top:652px;left:130px;font-size:32px;color:#222}
.about-text{left:132px;width:465px;font-size:11px;color:#555;line-height:19px}
.video-frame{top:660px;left:840px;width:260px;height:276px;border:6px solid var(--maroon)}
.video{top:694px;left:638px;width:422px;height:281px;background:linear-gradient(135deg,#e8e6e2,#c9c4bc 55%,#b8a897);}

/* categories */
.categories{top:1040px;left:80px;width:1120px;height:486px;background:var(--maroon);border-radius:80px 0 0 80px}
.cat-title{top:1170px;left:128px;color:var(--white);font-size:31px}
.cat-intro{top:1268px;left:136px;width:240px;color:var(--white);font-size:11.5px;line-height:19px}
.cat-btn{top:1354px;left:132px;width:175px;height:35px;background:var(--white);color:#222;font-weight:600}
.card{position:absolute;width:278px;height:186px;background:var(--maroon);box-shadow:0 3px 12px rgba(0,0,0,.3);color:var(--white);padding:0 22px}
.card .ico{position:absolute;left:32px;top:14px}
.card h3{position:absolute;top:64px;left:20px;font:400 15px "Tinos",serif;letter-spacing:.3px}
.card p{position:absolute;top:96px;left:22px;width:230px;font-size:11px;line-height:19px}
.card a{position:absolute;top:150px;left:24px;font-size:11.5px;font-weight:600;text-decoration:underline;color:var(--white)}

/* features */
.feat-title{top:1578px;left:0;width:1200px;text-align:center;font-size:31px;color:#222}
.feature{position:absolute;top:1698px;width:283px;height:185px;border-radius:4px;overflow:hidden}
.feature span{position:absolute;left:16px;bottom:34px;color:var(--white);font-size:14.5px;font-weight:600}

/* why */
.why{top:2028px;left:0;width:1118px;height:320px;background:var(--grey);border-radius:0 40px 80px 0}
.why-title{top:2086px;left:0;width:1118px;text-align:center;color:var(--white);font-size:30px}
.stat{position:absolute;top:2208px;width:200px;text-align:center;color:var(--white)}
.stat b{display:block;font-size:27px;font-weight:600}
.stat small{display:block;margin-top:6px;font-size:11px}

/* stories */
.stories-title{top:2404px;left:0;width:1200px;text-align:center;font-size:31px;color:#222}
.story{position:absolute;width:280px;height:250px;background:var(--white);box-shadow:0 2px 14px rgba(0,0,0,.12);padding:34px 24px 0}
.story p{font:400 11px "Roboto",sans-serif;color:#444;line-height:19px}
.story hr{border:0;height:1px;background:var(--maroon);width:46px;margin:20px 0 12px}
.story h4{font:400 14.5px "Roboto",sans-serif;color:#222}
.story small{font:400 10.5px "Roboto",sans-serif;color:#888}

/* contact */
.contact{top:2924px;left:80px;width:1120px;height:436px;background:var(--maroon);border-radius:80px 0 0 80px}
.contact-title{top:3036px;left:189px;color:var(--white);font-size:22px}
.contact-list{top:3088px;left:189px;color:var(--white);font-size:11px;line-height:25px}
.contact-list div{display:flex;gap:8px;align-items:center}
.contact-list svg{flex:none}
.newsletter{top:3036px;left:636px;width:470px;height:264px;background:var(--maroon);box-shadow:0 3px 14px rgba(0,0,0,.3);color:var(--white);text-align:center}
.newsletter h2{margin-top:16px;font-size:22px;line-height:32px}
.newsletter p{margin:6px auto 0;width:250px;font-size:11px;line-height:25px}
.newsletter .field{position:absolute;top:114px;left:109px;width:254px;height:40px;background:var(--white);color:#777;font-size:11px;text-align:left;padding:12px}
.newsletter .sub{top:172px;left:173px;width:125px;height:35px;background:var(--white);color:#222}

/* footer */
.follow{top:3422px;left:0;width:1200px;text-align:center;font-size:17px;color:#222}
.socials{top:3466px;left:514px;display:flex;gap:11px}
.socials i{width:25px;height:25px;border-radius:50%;background:var(--maroon)}
.copy{top:3518px;left:0;width:1200px;text-align:center;font-size:11px;color:#333}
</style>
</head>
<body>

<header class="abs topbar">
  <span style="left:131px">&#9742; 877-410-5526</span>
  <span style="left:236px;color:#fff">|</span>
  <span style="left:259px">&#9993; sales@lumawirehub.com</span>
  <span style="left:497px">Line Card</span>
  <span style="left:564px">|</span>
  <span style="left:583px">Gov/Edu Buyers</span>
  <span style="left:686px">|</span>
  <span style="left:705px">Resellers</span>
  <div class="auth" style="left:825px;width:110px"><i></i>LOGIN</div>
  <div class="auth" style="left:959px;width:111px"><i></i>REGISTER</div>
</header>

<nav class="abs nav">
  <div class="logo"><i></i>LWH</div>
  <div class="menu">
    <span class="active">HOME</span><span>ABOUT</span><span>ALL CATEGORIES</span><span>30 MIN QUOTE</span><span>PURCHASING</span>
  </div>
  <div class="search">Search Products
    <svg width="16" height="16" viewBox="0 0 16 16"><circle cx="7" cy="7" r="5" fill="none" stroke="#851639" stroke-width="1.5"/><line x1="11" y1="11" x2="15" y2="15" stroke="#851639" stroke-width="1.5"/></svg>
  </div>
  <svg class="abs" style="left:1044px;top:12px" width="22" height="20" viewBox="0 0 22 20"><path d="M1 2h4l3 11h10l3-8H6" fill="none" stroke="#851639" stroke-width="1.6"/><circle cx="9" cy="17" r="1.6" fill="#851639"/><circle cx="17" cy="17" r="1.6" fill="#851639"/></svg>
</nav>

<section class="abs hero" role="img" aria-label="Cable reel with orange fiber cable on grass beside a dug trench">
  <div class="shade"></div>
  <h1 class="display">LUMAWIRE HUB</h1>
  <p>Lorem ipsum dolor sit amet, consectetur adipiscing elit. Ut elit tellus, luctus nec ullamcorper mattis, pulvinar dapibus leo.</p>
  <div class="btn" style="top:299px;left:538px;width:125px;height:34px">VIEW MORE</div>
</section>

<h2 class="abs display about-title">ABOUT US</h2>
<div class="divider" style="top:698px;left:134px;color:var(--maroon)"><b></b><i style="width:50px"></i></div>
<p class="abs about-text" style="top:737px">Lorem Ipsum is simply dummy text of the printing and typesetting industry. Lorem Ipsum has been the industry's standard dummy text ever since the 1500s, when an unknown printer took a galley of type and scrambled</p>
<p class="abs about-text" style="top:812px">Lorem Ipsum is simply dummy text of the printing and typesetting industry. Lorem Ipsum has been the industry's standard dummy text ever since the 1500s, when an unknown printer took a galley of type and scrambled it to make a type specimen book. It has survived not only five centuries, but also the leap into electronic type setting, remaining essentially unchanged. It was popularised.</p>
<div class="btn" style="top:939px;left:131px;width:126px;height:36px">VIEW MORE</div>
<div class="abs video-frame"></div>
<a class="abs video" href="https://www.vidstreamo.com/watch?v=Q4-RtPw7z2M" role="img" aria-label="Video: hands holding a fiber patch cable with LC connectors"></a>

<section class="abs categories"></section>
<h2 class="abs display cat-title">CATEGORIES</h2>
<div class="divider" style="top:1229px;left:140px;color:var(--white)"><b></b><i style="width:62px"></i></div>
<p class="abs cat-intro">Lorem Ipsum is simply dummy text of the printing and typesetting industry. Lorem Ipsum has been the industry's standard</p>
<div class="btn cat-btn">VIEW ALL CATEGORIES</div>

<div class="card" style="top:1090px;left:460px">
  <svg class="ico" width="46" height="30" viewBox="0 0 46 30"><rect x="1" y="10" width="14" height="10" fill="none" stroke="#fff" stroke-width="1.5"/><path d="M15 12l30-10M15 15l30-6M15 18l30 0M15 20l30 6" stroke="#fff" stroke-width="1.3" fill="none"/></svg>
  <h3>ANY ANGLE FIBER PATCH</h3>
  <p>Lorem Ipsum is simply dummy text of the printing and typesetting industry.</p>
  <a>VIEW ALL</a>
</div>
<div class="card" style="top:1090px;left:786px">
  <svg class="ico" width="46" height="40" viewBox="0 0 46 40"><path d="M4 2v38" stroke="#fff" stroke-width="1.5"/><rect x="8" y="12" width="14" height="14" fill="none" stroke="#fff" stroke-width="1.5"/><path d="M22 14h20M22 19h20M22 24h20" stroke="#fff" stroke-width="1.3"/></svg>
  <h3>OS2 SINGLE MIODE</h3>
  <p>Lorem Ipsum is simply dummy text of the printing and typesetting industry.</p>
  <a>VIEW ALL</a>
</div>
<div class="card" style="top:1291px;left:460px">
  <svg class="ico" width="64" height="30" viewBox="0 0 64 30"><rect x="2" y="6" width="60" height="5" fill="none" stroke="#fff" stroke-width="1.5"/><rect x="2" y="18" width="60" height="5" fill="none" stroke="#fff" stroke-width="1.5"/><path d="M44 2v13M44 15v13" stroke="#fff" stroke-width="1.5"/></svg>
  <h3>OMI MULTIMODE</h3>
  <p>Lorem Ipsum is simply dummy text of the printing and typesetting industry.</p>
  <a>VIEW ALL</a>
</div>
<div class="card" style="top:1291px;left:786px">
  <svg class="ico" width="46" height="30" viewBox="0 0 46 30"><rect x="1" y="10" width="14" height="10" fill="none" stroke="#fff" stroke-width="1.5"/><path d="M15 12l30-10M15 15l30-6M15 18l30 0M15 20l30 6" stroke="#fff" stroke-width="1.3" fill="none"/></svg>
  <h3>OM2 MULTIMODE</h3>
  <p>Lorem Ipsum is simply dummy text of the printing and typesetting industry.</p>
  <a>VIEW ALL</a>
</div>

<h2 class="abs display feat-title">FEATURES</h2>
<div class="divider" style="top:1635px;left:545px;color:var(--maroon)"><i></i><b></b><i></i></div>
<div class="feature" style="left:133px;background:linear-gradient(135deg,#e8a050,#d97b3a 45%,#3a8aa0 80%,#2a4a5a)" role="img" aria-label="Orange fiber patch cables with blue connectors"><span>Full Fiber Flexibility</span></div>
<div class="feature" style="left:460px;background:linear-gradient(135deg,#3a3633,#6a5e55 50%,#2c2a28)" role="img" aria-label="Technician splicing fiber with a tool"><span>FAST All Over Again!</span></div>
<div class="feature" style="left:786px;background:linear-gradient(135deg,#4a4a46,#7a7a70 50%,#3a3a36)" role="img" aria-label="Fiber test meter held in hands"><span>Gov,Military Preferred Pricing</span></div>
<div class="btn" style="top:1930px;left:538px;width:125px;height:35px">VIEW MORE</div>

<section class="abs why"></section>
<h2 class="abs display why-title">WHY CHOOSE US?</h2>
<div class="divider" style="top:2140px;left:485px;color:var(--white)"><i></i><b></b><i></i></div>
<div class="stat" style="left:127px"><b>5K+</b><small>Products</small></div>
<div class="stat" style="left:364px"><b>20+</b><small>Years Experience</small></div>
<div class="stat" style="left:602px"><b>3000+</b><small>Satisfied Clients</small></div>
<div class="stat" style="left:839px"><b>30+</b><small>Branches</small></div>

<h2 class="abs display stories-title">OUR SUCCESS STORIES</h2>
<div class="divider" style="top:2459px;left:545px;color:var(--maroon)"><i></i><b></b><i></i></div>
<div class="story" style="top:2518px;left:132px">
  <p>Lorem ipsum dolor sit amet, consectetur adipiscing elit. Quisque arcu ante, egestas ut ullamcorper sed, aliquam et odio. Sed ac interdum eros, ac semper lorem. Praesent at ipsum molestie, facilisis lacus porta, vulputate purus. Maecenas id neque ut turpis faucibus porta.</p>
  <hr><h4>Daniel Morrow</h4><small>NQR Electronics</small>
</div>
<div class="story" style="top:2605px;left:460px">
  <p>Lorem ipsum dolor sit amet, consectetur adipiscing elit. Quisque arcu ante, egestas ut ullamcorper sed, aliquam et odio. Sed ac interdum eros, ac semper lorem. Praesent at ipsum molestie, facilisis lacus porta, vulputate purus. Maecenas id neque ut turpis faucibus porta.</p>
  <hr><h4>Ravel</h4><small>ABC Electronics</small>
</div>
<div class="story" style="top:2518px;left:782px">
  <p>Lorem ipsum dolor sit amet, consectetur adipiscing elit. Quisque arcu ante, egestas ut ullamcorper sed, aliquam et odio. Sed ac interdum eros, ac semper lorem. Praesent at ipsum molestie, facilisis lacus porta, vulputate purus. Maecenas id neque ut turpis faucibus porta.</p>
  <hr><h4>Lucas</h4><small>XYZ Electronics</small>
</div>

<section class="abs contact"></section>
<h2 class="abs display contact-title">CONTACT INFORMATION</h2>
<div class="abs contact-list">
  <div><svg width="12" height="14" viewBox="0 0 12 14"><path d="M6 13S1 7.5 1 5a5 5 0 0110 0c0 2.5-5 8-5 8z" fill="#fff"/><circle cx="6" cy="5" r="1.8" fill="#851639"/></svg>LWH Sales Office | Warehouse ,</div>
  <div style="padding-left:20px">2480 Harbor Ridge Rd.</div>
  <div style="padding-left:20px">Suite C | LAKEWOOD, CA 90712 - 2204</div>
  <div><svg width="13" height="13" viewBox="0 0 13 13"><circle cx="6.5" cy="6.5" r="5.5" fill="none" stroke="#fff" stroke-width="1.4"/><path d="M6.5 3.5v3h2.5" stroke="#fff" stroke-width="1.3" fill="none"/></svg>Hours: 8:00am - 5:00pm / Mon-Fri</div>
  <div><svg width="13" height="10" viewBox="0 0 13 10"><rect width="13" height="10" rx="1" fill="#fff"/><path d="M0 1l6.5 5L13 1" stroke="#851639" fill="none"/></svg>sales@lumawirehub.com</div>
  <div><svg width="13" height="13" viewBox="0 0 13 13"><rect width="13" height="13" rx="2" fill="#fff"/><path d="M4 3l1.5 2-1 1c.6 1.2 1.3 1.9 2.5 2.5l1-1 2 1.5-1 1.5C6 10 3 7 2.5 4z" fill="#851639"/></svg>Call us now: (877) 410-5526</div>
</div>
<div class="abs newsletter">
  <h2 class="display">NEWSLETTER</h2>
  <p>Signup for our newsletter and receive great deals on our products.</p>
  <div class="field">Enter Your Email Address</div>
  <div class="btn sub">SUBSCRIBE</div>
</div>

<h2 class="abs display follow">FOLLOW US ON</h2>
<div class="abs socials"><i></i><i></i><i></i><i></i><i></i></div>
<p class="abs copy">Copyright © 2021 - <b>LumaWire Hub</b>, Inc. All Right Reserved</p>

</body>
</html>
```